Pale Harbor - post rock band album cover design

We are Pale Harbor, a post-rock band based on San Jose, CA, USA. We will release a new album “Where the rivers fold" and need a album cover.

The new album is full of emotion and energy. song list:
1. Forward
2. Search (in uploaded files)
3. Before
4. Memory
5. Dream
6. Spring
7. Om Namah Shivaya

Please hear our previous music here
https://pale-harbor.tunecrate-demo.net/album/pale-harbor

Target Market(s)

music lovers

Industry/Entity Type

Music Download

Colors

Requirements
Must have
• album cover + back
• For cover we only need band name (do not need album name), want to use some streamline font for the band name "Pale Harbor"
• I attached an example from another band
Nice to have
• I don't want to limit the designers, so please listen to the music and design what you feel the best:)

```html
<!DOCTYPE html>
<html lang="en">
<head>
<meta charset="utf-8">
<title>Pale Harbor — Where the rivers fold — Back Cover</title>
<link rel="stylesheet" href="https://fonts.googleapis.com/css2?family=Poiret+One&display=swap">
<style>
  :root {
    --page: #ffffff;
    --navy: #1e1c5a;
    --deep-teal: #1d4a58;
    --emerald: #22b04f;
    --lime: #6dbf45;
    --leaf: #58bb48;
    --olive: #8c8a36;
    --ember: #d9452a;
    --ink-light: #f3f7ee;
  }
  html, body {
    margin: 0;
    padding: 0;
    width: 1200px;
    height: 1200px;
    overflow: hidden;
    background: var(--page);
  }
  .canvas {
    position: relative;
    width: 1200px;
    height: 1200px;
    background: var(--page);
  }
  .back-cover {
    position: absolute;
    left: 150px;
    top: 150px;
    width: 842px;
    height: 843px;
    overflow: hidden;
  }
  .back-cover__gradient {
    position: absolute;
    inset: 0;
    width: 100%;
    height: 100%;
    display: block;
  }
  .tracklist-frame {
    position: absolute;
    left: 123px;
    top: 78px;
    width: 593px;
    height: 689px;
    border: 1.5px solid var(--ink-light);
    box-sizing: border-box;
  }
  .tracklist {
    position: absolute;
    left: 160px;
    top: 160px;
    margin: 0;
    padding: 0;
    list-style: none;
    font-family: "Poiret One", sans-serif;
    font-size: 29px;
    line-height: 41px;
    letter-spacing: 0.5px;
    color: var(--ink-light);
    text-transform: uppercase;
    white-space: nowrap;
  }
  .tracklist__paren {
    font-size: 34px;
  }
</style>
</head>
<body>
  <main class="canvas">
    <section class="back-cover" aria-label="Pale Harbor, Where the rivers fold — back cover">
      <svg class="back-cover__gradient" viewBox="0 0 842 843" preserveAspectRatio="none" aria-hidden="true">
        <defs>
          <linearGradient id="field" x1="0" y1="0" x2="0" y2="1">
            <stop offset="0" stop-color="var(--navy)"/>
            <stop offset="0.08" stop-color="var(--navy)"/>
            <stop offset="0.17" stop-color="var(--deep-teal)"/>
            <stop offset="0.27" stop-color="var(--emerald)"/>
            <stop offset="0.4" stop-color="var(--lime)"/>
            <stop offset="0.62" stop-color="var(--leaf)"/>
            <stop offset="1" stop-color="var(--olive)"/>
          </linearGradient>
          <linearGradient id="ember" x1="0.3" y1="0.55" x2="0.95" y2="1">
            <stop offset="0" stop-color="var(--ember)" stop-opacity="0"/>
            <stop offset="0.35" stop-color="#b0713a" stop-opacity="0.6"/>
            <stop offset="1" stop-color="var(--ember)" stop-opacity="1"/>
          </linearGradient>
          <filter id="soften" x="-20%" y="-50%" width="140%" height="200%">
            <feGaussianBlur stdDeviation="28"/>
          </filter>
        </defs>
        <rect width="842" height="843" fill="url(#field)"/>
        <path d="M-60 -40 H900 V70 C760 40 600 90 420 95 C260 100 120 150 -60 190 Z"
              fill="var(--navy)" opacity="0.9" filter="url(#soften)"/>
        <rect width="842" height="843" fill="url(#ember)"/>
      </svg>
      <div class="tracklist-frame"></div>
      <ol class="tracklist">
        <li>1. Forward</li>
        <li>2. Search <span class="tracklist__paren">(</span>in uploaded files<span class="tracklist__paren">)</span></li>
        <li>3. Before</li>
        <li>4. Memory</li>
        <li>5. Dream</li>
        <li>6. Spring</li>
        <li>7. Om Namah Shivaya</li>
      </ol>
    </section>
  </main>
</body>
</html>
```